QAT Methodology infographic that shows flow of the process outlined on our web site

We are looking for a graphical representation of the methodology that is described on this web page: https://www.qat-example.com/about-qat/methodology/ We would like someone to be able to quickly understand our methodology and the key points outlined on the web page - the graphic should be able to do that.

Target Market(s)

Enterprise Companies with 1000+ employees

Industry/Entity Type

Information Technology

Font styles to use
Sans Serif

Colors
3277b5
abd036
faa54b

Requirements
Must have
• Must convey the method/process with enough detail to understand what the process is.
Nice to have
• Arrows or something showing flow would be great
Should not have
• Should not be "cartoony"

```html
<!DOCTYPE html>
<html lang="en">
<head>
<meta charset="utf-8">
<title>QAT Methodology</title>
<link rel="stylesheet" href="https://fonts.googleapis.com/css2?family=Archivo+Narrow:wght@700&family=PT+Sans:wght@400&display=swap">
<style>
  :root {
    --blue: #3277b5;
    --green: #abd036;
    --orange: #faa54b;
    --ink: #231f20;
    --tag: #dfe3e4;
    --paper: #ffffff;
  }
  html, body {
    margin: 0;
    padding: 0;
    overflow: hidden;
    background: var(--paper);
  }
  .canvas {
    position: relative;
    width: 1200px;
    height: 840px;
    overflow: hidden;
    background: var(--paper);
  }
  .flow {
    position: absolute;
    left: 0;
    top: 0;
    width: 1200px;
    height: 840px;
  }
  .step-number {
    font-family: "Archivo Narrow", "Arial Narrow", sans-serif;
    font-weight: 700;
    font-size: 34px;
    text-anchor: middle;
  }
  .step-text {
    position: absolute;
    text-align: center;
    transform: translateX(-50%);
  }
  .step-title {
    margin: 0 0 4px;
    font-family: "Archivo Narrow", "Arial Narrow", sans-serif;
    font-weight: 700;
    font-size: 22px;
    letter-spacing: 0.5px;
    text-transform: uppercase;
  }
  .step-body {
    margin: 0;
    font-family: "PT Sans", Arial, sans-serif;
    font-size: 15.4px;
    line-height: 18.6px;
    color: var(--ink);
    white-space: nowrap;
  }
  .step-text--consultation { left: 258px; top: 568px; }
  .step-text--assessment   { left: 498px; top: 74px; }
  .step-text--solution     { left: 738px; top: 568px; }
  .step-text--implementation { left: 978px; top: 128px; }
  .step-text--consultation .step-title,
  .step-text--implementation .step-title { color: var(--blue); }
  .step-text--assessment .step-title { color: var(--green); }
  .step-text--solution .step-title { color: var(--orange); }
</style>
</head>
<body>
<main class="canvas">
  <svg class="flow" viewBox="0 0 1000 700" aria-hidden="true">
    <!-- flow line -->
    <g fill="none" stroke-width="13" stroke-linejoin="miter">
      <polyline stroke="var(--blue)" points="88,343 112,343 112,395 215,452 318,395 318,350"/>
      <polyline stroke="var(--green)" points="318,352 318,290 415,233 512,290 512,352"/>
      <polyline stroke="var(--orange)" points="512,348 512,400 612,457 712,400 712,348"/>
      <polyline stroke="var(--blue)" points="712,352 712,290 812,233 912,290 912,350 937,350"/>
    </g>

    <!-- step 1 -->
    <rect x="158" y="302" width="114" height="36" fill="var(--tag)"/>
    <text class="step-number" x="215" y="333" fill="var(--blue)">1</text>
    <polygon points="158,350 272,350 272,392 215,425 158,392" fill="var(--blue)"/>
    <g fill="none" stroke="#fff" stroke-width="3" stroke-linejoin="round">
      <path d="M196,362 h30 a3,3 0 0 1 3,3 v14 a3,3 0 0 1 -3,3 h-16 l-8,7 v-7 h-6 a3,3 0 0 1 -3,-3 v-14 a3,3 0 0 1 3,-3z"/>
      <line x1="202" y1="370" x2="222" y2="370"/>
      <line x1="202" y1="376" x2="216" y2="376"/>
    </g>

    <!-- step 2 -->
    <polygon points="357,298 415,265 472,298 472,340 357,340" fill="var(--green)"/>
    <g fill="none" stroke="#fff" stroke-width="3">
      <path d="M398,285 h20 l6,6 v30 h-26z" stroke-linejoin="round"/>
      <circle cx="414" cy="305" r="8"/>
      <line x1="420" y1="311" x2="428" y2="320" stroke-linecap="round"/>
    </g>
    <rect x="357" y="348" width="115" height="35" fill="var(--tag)"/>
    <text class="step-number" x="415" y="378" fill="var(--green)">2</text>

    <!-- step 3 -->
    <rect x="555" y="302" width="115" height="36" fill="var(--tag)"/>
    <text class="step-number" x="612" y="333" fill="var(--orange)">3</text>
    <polygon points="555,350 670,350 670,392 612,425 555,392" fill="var(--orange)"/>
    <g fill="none" stroke="#fff" stroke-width="3" stroke-linecap="round">
      <path d="M605,391 v-5 a12,12 0 1 1 14,0 v5z" stroke-linejoin="round"/>
      <line x1="606" y1="396" x2="618" y2="396"/>
      <line x1="612" y1="354" x2="612" y2="358"/>
      <line x1="594" y1="362" x2="597" y2="365"/>
      <line x1="630" y1="362" x2="627" y2="365"/>
      <line x1="588" y1="376" x2="592" y2="376"/>
      <line x1="636" y1="376" x2="632" y2="376"/>
    </g>

    <!-- step 4 -->
    <polygon points="757,298 815,265 872,298 872,340 757,340" fill="var(--blue)"/>
    <g stroke="#fff" fill="none">
      <circle cx="808" cy="306" r="11" stroke-width="6" stroke-dasharray="4 3"/>
      <circle cx="808" cy="306" r="6" stroke-width="3"/>
      <line x1="818" y1="296" x2="832" y2="284" stroke-width="4" stroke-linecap="round"/>
      <line x1="822" y1="316" x2="834" y2="328" stroke-width="5" stroke-linecap="round"/>
    </g>
    <rect x="757" y="348" width="115" height="35" fill="var(--tag)"/>
    <text class="step-number" x="815" y="378" fill="var(--blue)">4</text>
  </svg>

  <section class="step-text step-text--assessment">
    <h2 class="step-title">Assessment</h2>
    <p class="step-body">Very often after an initial consultation<br>is over, the process is best served by adding<br>an assessment phase. This process can range from<br>simple interviews to full enterprise evaluations.<br>The assessment stage should end with the discovery<br>of all pertinent information needed for the<br>development of an effective solution.</p>
  </section>

  <section class="step-text step-text--implementation">
    <h2 class="step-title">Implementation</h2>
    <p class="step-body">Upon acceptance of a quote<br>and a subsequent purchase order,<br>the certified QAT engineers<br>proceed with your implementation.</p>
  </section>

  <section class="step-text step-text--consultation">
    <h2 class="step-title">Initial Consultation</h2>
    <p class="step-body">A first conversation in any relationship is<br>vitally important. This is especially true when<br>beginning an IT project. Setting expectations<br>and defining success are integral parts of the<br>process. An initial consultation with QAT will be<br>filled with questions and listening as we discover<br>the concerns you have and consider the best<br>approach to help you achieve your goals.</p>
  </section>

  <section class="step-text step-text--solution">
    <h2 class="step-title">Solution Development</h2>
    <p class="step-body">Your QAT team includes members of<br>the account management, engineering,<br>and finance departments. After initial<br>consultations and assessments are completed,<br>your team convenes to design and draw up<br>solutions for your consideration.</p>
  </section>
</main>
</body>
</html>
```